Design some Business Cards

I NEED A BUSINESS CARD. (TWO SIDE DESIGN) . PLEASE USE THE FOLLOWING INFORMATION AND LOGO. THANKS.
Name: Malek Ostrowicz (Owner)
Bus Tel.: (416) 555-0173
Cell: 416 555 0288
Email: info@bluecoveinc.example
Web: bluecoveinc.example
Address: 287 Pellbrook Road Unit 41. Toronto, ON M0X 9Z9. Scarborough.

```html
<!DOCTYPE html>
<html lang="en">
<head>
<meta charset="utf-8">
<title>Blue Cove Homestore – Business Card</title>
<link href="https://fonts.googleapis.com/css2?family=Open+Sans:wght@400;600;700&display=swap" rel="stylesheet">
<style>
  :root {
    --stage: #3b3637;
    --paper: #ffffff;
    --ink-dark: #141414;
    --accent: #e2343f;
    --text-grey: #5a5a5a;
    --text-dark: #2b2b2b;
  }
  * { margin: 0; padding: 0; box-sizing: border-box; }
  html, body {
    width: 1200px; height: 675px; overflow: hidden;
    background: var(--stage);
    font-family: "Open Sans", Arial, sans-serif;
  }
  .stage {
    width: 1200px; height: 675px;
    display: flex; align-items: center; justify-content: center; gap: 60px;
  }
  .card {
    position: relative;
    width: 520px; height: 297px;
    overflow: hidden;
    box-shadow: 0 10px 30px rgba(0,0,0,.35);
  }

  /* Front side */
  .card--front { background: var(--paper); }
  .brand {
    position: absolute; display: flex; align-items: center; gap: 10px;
    color: var(--accent); font-weight: 700; letter-spacing: .06em;
    text-transform: uppercase;
  }
  .brand__mark { background: var(--accent); flex: none; }
  .card--front .brand { left: 36px; top: 44px; font-size: 22px; }
  .card--front .brand__mark { width: 18px; height: 18px; }
  .front__rule {
    position: absolute; left: 36px; right: 0; top: 118px;
    height: 5px; background: var(--accent);
  }
  .holder { position: absolute; left: 36px; top: 140px; }
  .holder__name { color: var(--accent); font-weight: 600; font-size: 22px; line-height: 1.2; }
  .holder__role { color: var(--text-grey); font-size: 17px; line-height: 1.3; }
  .contact {
    position: absolute; left: 36px; right: 24px; top: 214px;
    font-size: 10.5px; line-height: 1.7; color: var(--text-dark);
  }
  .contact__label { color: var(--accent); }

  /* Back side */
  .card--back { background: var(--ink-dark); }
  .back__rule {
    position: absolute; left: 0; top: 176px; width: 170px;
    height: 2px; background: var(--accent);
  }
  .card--back .brand {
    left: 190px; top: 118px; font-size: 26px;
  }
  .card--back .brand__mark { width: 22px; height: 22px; }
  .back__web {
    position: absolute; right: 24px; bottom: 20px;
    font-size: 10.5px; color: var(--accent);
  }
</style>
</head>
<body>
  <main class="stage">
    <section class="card card--front" aria-label="Business card front">
      <div class="brand"><span class="brand__mark"></span>Blue Cove Homestore</div>
      <div class="front__rule"></div>
      <div class="holder">
        <p class="holder__name">Malek Ostrowicz</p>
        <p class="holder__role">(Owner)</p>
      </div>
      <div class="contact">
        <p><span class="contact__label">Address:</span> 287 Pellbrook Road Unit 41, Toronto, ON M0X 9Z9, Scarborough.</p>
        <p><span class="contact__label">Bus Telephone:</span> (416) 555-0173 &nbsp;<span class="contact__label">Phone:</span> 416 555 0288 &nbsp;<span class="contact__label">mail:</span> info@bluecoveinc.example</p>
      </div>
    </section>

    <section class="card card--back" aria-label="Business card back">
      <div class="back__rule"></div>
      <div class="brand"><span class="brand__mark"></span>Blue Cove Homestore</div>
      <p class="back__web">Website: bluecoveinc.example</p>
    </section>
  </main>
</body>
</html>
```